Cobalt Bridge Capital - Letterhead

We need letterhead options for our case funding company called Cobalt Bridge Capital. Here are some of the details:

Name - Cobalt Bridge Capital
Phone - (555) 214 - 9087
Address - 58 Harlow Lane
Suite 312
New York, NY 10482
Website - cobaltbridgecapital.example

```html
<!DOCTYPE html>
<html lang="en">
<head>
<meta charset="utf-8">
<title>Cobalt Bridge Capital – Letterhead</title>
<link href="https://fonts.googleapis.com/css2?family=Questrial&family=Roboto:wght@400&display=swap" rel="stylesheet">
<style>
  :root {
    --backdrop: #e6e7e8;
    --paper-light: #f7f7f8;
    --paper-dark: #e4e5e6;
    --navy: #0c2f4f;
    --slate: #566b7c;
    --mist: #98a3ad;
    --ink: #4a4a4a;
    --ink-soft: #5a5a5a;
    --signature-blue: #3b6fb6;
  }
  * { margin: 0; padding: 0; box-sizing: border-box; }
  html, body {
    width: 1024px; height: 1200px; overflow: hidden;
    background: var(--backdrop);
  }
  .letterhead {
    position: absolute; left: 142px; top: 80px;
    width: 740px; height: 1040px;
    background: linear-gradient(90deg, var(--paper-light) 0%, var(--paper-dark) 100%);
    box-shadow: 0 6px 24px rgba(0,0,0,0.12);
    font-family: "Questrial", sans-serif;
    color: var(--ink);
  }
  .brand {
    position: absolute; left: 70px; top: 66px;
    display: flex; align-items: flex-start; gap: 12px;
  }
  .brand-square {
    width: 56px; height: 56px; background: var(--navy);
  }
  .brand-name {
    font-family: "Questrial", sans-serif;
    font-size: 17px; line-height: 19px; letter-spacing: 1px;
    text-transform: uppercase; color: var(--navy);
    padding-top: 1px;
  }
  .contact {
    position: absolute; left: 577px; top: 88px;
    font-family: "Roboto", sans-serif; font-size: 11.5px; line-height: 13.5px;
    color: var(--ink-soft);
  }
  .contact .phone { margin-top: 5px; display: flex; align-items: center; gap: 6px; }
  .contact .phone svg { width: 10px; height: 10px; fill: var(--navy); }
  .letter-body {
    position: absolute; left: 70px; top: 278px; width: 612px;
  }
  .salutation { font-size: 18px; color: var(--ink-soft); margin-bottom: 26px; }
  .letter-body p {
    font-size: 10.4px; line-height: 13.4px; color: var(--ink);
    text-align: left; margin-bottom: 13px;
  }
  .closing { margin-top: 25px; }
  .signature {
    position: absolute; left: 70px; top: 712px; width: 126px; height: 62px;
    background: linear-gradient(90deg, rgba(59,111,182,0.18), rgba(59,111,182,0.08));
    border-radius: 4px;
  }
  .website {
    position: absolute; left: 0; right: 0; top: 963px; text-align: center;
    font-family: "Roboto", sans-serif; font-size: 11px; letter-spacing: 3.6px;
    color: var(--ink-soft);
  }
  .footer-bands {
    position: absolute; left: 0; right: 0; bottom: 4px; height: 11px;
    display: flex; gap: 2px;
  }
  .footer-bands span { flex: 1; }
  .band-navy { background: var(--navy); }
  .band-slate { background: var(--slate); }
  .band-mist { background: var(--mist); }
</style>
</head>
<body>
  <main class="letterhead">
    <div class="brand">
      <div class="brand-square"></div>
      <div class="brand-name">Cobalt<br>Bridge<br>Capital</div>
    </div>

    <address class="contact" style="font-style:normal">
      58 Harlow Lane<br>
      Suite 312<br>
      New York, NY 10482
      <div class="phone">
        <svg viewBox="0 0 24 24" aria-hidden="true"><path d="M6.6 10.8c1.4 2.8 3.8 5.1 6.6 6.6l2.2-2.2c.3-.3.7-.4 1-.2 1.1.4 2.3.6 3.6.6.6 0 1 .4 1 1V20c0 .6-.4 1-1 1C10.6 21 3 13.4 3 4c0-.6.4-1 1-1h3.5c.6 0 1 .4 1 1 0 1.3.2 2.5.6 3.6.1.3 0 .7-.2 1l-2.3 2.2z"/></svg>
        (555) 214 - 9087
      </div>
    </address>

    <section class="letter-body">
      <h1 class="salutation" style="font-weight:normal">Dear Mr. Carter,</h1>
      <p>Lorem ipsum dolor sit amet, consectetur adipiscing elit. Donec orci purus, luctus vitae dignissim eu, iaculis sed purus. Vivamus faucibus, ipsum nec aliquet viverra, leo mauris condimentum ligula, sit amet sagittis enim ligula quis arcu. Nam egestas tortor id nisi porttitor mattis. In tortor ante, ultricies in suscipit a, tempus non massa. Vivamus et auctor mi. Fusce vel massa nulla. Phasellus nec eros mauris, et scelerisque orci.</p>
      <p>Donec malesuada orci vitae nulla accumsan porta a id massa. Quisque accumsan iaculis magna sit amet fringilla. Maecenas consequat, magna eget tincidunt semper, odio nibh rutrum mi, id feugiat ante nisi eu risus. Vestibulum nunc orci, rhoncus a placerat in, ultricies in mi. Cras mattis varius eros, vel fringilla nisi suscipit eget. Quisque scelerisque sagittis nulla at porttitor.</p>
      <p>Sed id augue vitae urna euismod commodo aliquet a quam. Pellentesque arcu velit, cursus et malesuada ut, consequat et diam. Nullam erat sem, rhoncus id ullamcorper vitae, rhoncus et arcu. In ultricies ultricies nulla, ut rutrum nisi iaculis at. Donec eu magna a metus ornare faucibus. Fusce aliquet faucibus ultricies. Morbi semper, est id tincidunt gravida, sem arcu adipiscing lacus, ac bibendum nulla leo eu purus. Quisque nec diam sed risus consectetur a ccumsan quis quis nibh. Vestibulum id purus lorem.</p>
      <p>It is a long established fact that a reader will be distracted by the readable content of a page when looking at its layout. The point of using Lorem Ipsum is that it has a more-or-less normal distribution of letters, as opposed to using 'Content here, content here', making it look like readable English. Many desktop publishing packages</p>
      <p class="closing">Sincerely,</p>
    </section>

    <div class="signature" role="img" aria-label="Handwritten signature of Evan Carter in blue ink"></div>

    <div class="website">www.cobaltbridgecapital.example</div>

    <div class="footer-bands">
      <span class="band-navy"></span>
      <span class="band-slate"></span>
      <span class="band-mist"></span>
    </div>
  </main>
</body>
</html>
```